Healer at the Hearth needs business card

We need a business card that reflects the look and feel of the new website at www.healerathehearth.ca

Our patient navigation and advocacy services are most commonly used by seniors who feel overwhelmed by the health care system and want someone on their side to advocate for their care. Individuals with ill parents or other family members may also come to rely on Healer at the Hearth to help them support their loved one through their health care journey. Ultimately, anyone who finds their health care experience challenging and wants someone completely focused on their needs can benefit from the services of our doctor / nurse team.

Business

Must have
• One design tailored for two clinician which should include: logo, name, title, tel, email, web address and tagline
Nice to have
• A banner image to create a similar look to the website at www.healerathehearth.ca
Should not have
• Too cluttered or busy - must be clean and professional

```html
<!DOCTYPE html>
<html lang="en">
<head>
<meta charset="utf-8">
<title>Healer at the Hearth – Business Card</title>
<link rel="stylesheet" href="https://fonts.googleapis.com/css2?family=Ubuntu:wght@400&family=Gelasio:ital,wght@0,400;1,400&display=swap">
<style>
  :root {
    --page-bg: #d9d9d9;
    --card-bg: #ffffff;
    --brand-red: #a3182c;
    --brand-blue: #2f6294;
    --ink: #2b2b2b;
    --photo-light: #e4eef6;
    --photo-mid: #bcd3e6;
    --photo-warm: #e6b89a;
    --photo-teal: #3fb3a4;
  }
  * { box-sizing: border-box; margin: 0; padding: 0; }
  html, body {
    width: 1200px; height: 900px; overflow: hidden;
    background: var(--page-bg);
  }
  .card-set {
    position: absolute; inset: 0;
    display: flex; align-items: center; justify-content: center; gap: 60px;
  }
  .card {
    position: relative;
    width: 520px; height: 297px;
    background: var(--card-bg);
    box-shadow: 0 6px 18px rgba(0,0,0,0.18);
    overflow: hidden;
  }
  /* Contact side */
  .card--contact .banner-photo {
    position: absolute; left: 0; top: 0;
    width: 100%; height: 206px;
    background:
      linear-gradient(160deg, transparent 40%, var(--photo-warm) 55%, transparent 70%),
      linear-gradient(200deg, transparent 10%, var(--photo-teal) 18%, transparent 28%),
      linear-gradient(120deg, var(--photo-light), var(--photo-mid) 60%, var(--photo-light));
  }
  .card--contact .brand-tag {
    position: absolute; right: 0; top: 0;
    width: 190px; height: 60px;
    background: var(--card-bg);
    display: flex; align-items: center; gap: 8px; padding-left: 14px;
  }
  .brand-dot {
    flex: none; border-radius: 50%; background: var(--brand-red);
  }
  .brand-tag .brand-dot { width: 26px; height: 26px; }
  .brand-name {
    font-family: "Ubuntu", sans-serif; font-weight: 400;
    color: var(--brand-blue); line-height: 1.0;
  }
  .brand-tag .brand-name { font-size: 17px; }
  .contact-block {
    position: absolute; left: 18px; right: 18px; top: 220px;
    font-family: "Gelasio", serif; font-size: 18px; line-height: 1.5;
    color: var(--ink); white-space: nowrap;
  }
  .contact-block .label { color: var(--brand-red); }

  /* Brand side */
  .card--brand .brand-lockup {
    position: absolute; left: 56px; top: 36px;
    display: flex; align-items: center; gap: 24px;
  }
  .card--brand .brand-dot { width: 96px; height: 96px; }
  .card--brand .brand-name { font-size: 46px; line-height: 0.95; }
  .tagline {
    position: absolute; left: 56px; right: 30px; top: 160px;
    font-family: "Gelasio", serif; font-size: 19px; line-height: 1.2;
    color: var(--ink);
  }
  .clinicians {
    position: absolute; left: 56px; right: 30px; top: 222px;
    list-style: none;
    font-family: "Gelasio", serif; font-size: 15px; line-height: 1.4;
    color: var(--ink);
  }
  .clinicians .title { color: var(--brand-red); }
</style>
</head>
<body>
  <main class="card-set">
    <section class="card card--contact">
      <div class="banner-photo" role="img" aria-label="Photo of a caregiver's hands gently holding a patient's hand"></div>
      <div class="brand-tag">
        <span class="brand-dot"></span>
        <span class="brand-name">Healer at<br>the Hearth</span>
      </div>
      <div class="contact-block">
        <p class="contact-line"><span class="label">Call:</span> 555-014-2236, <span class="label">Email:</span> info@healerathehearth.ca</p>
        <p class="web-line"><span class="label">Web:</span> www.healerathehearth.ca</p>
      </div>
    </section>

    <section class="card card--brand">
      <div class="brand-lockup">
        <span class="brand-dot"></span>
        <span class="brand-name">Healer at<br>the Hearth</span>
      </div>
      <p class="tagline">“best possible health care for you and<br>your loved ones”</p>
      <ul class="clinicians">
        <li>Dr. Maren Holt, <span class="title">Physician Advocate</span></li>
        <li>Priya Okafor, RN, <span class="title">Nurse Navigator</span></li>
      </ul>
    </section>
  </main>
</body>
</html>
```